GoalDash Arena - App Graphics Design

Context
-
Our company has launched an inplay mobile game app - where players can predict in real-time what will happen next during live football matches.
The game is called GoalDash Arena and currently has the following online resources:
Sociallounge Page: http://www.sociallounge.example/pages/GoalDash-Arena/418275093618264
iOS App: http://apps.orchardstore.example/us/app/goaldash-arena/id607193845?mt=8
Android App: https://market.droidshelf.example/store/apps/details?id=com.goaldasharena.android
The Project
-
This project involves creating enhanced graphics for the app - based on the current functional layout (see screenshots).
The graphics should be consistent throughout the game, and the design should improve the look and feel for the end user.
The designs should do as follows:
- Continue to enable the full functionality shown in the current screenshots
- Feel free to change any / all colour schemes / layouts / designs / graphics
- Look good to a sports fan user
Updates
I have just increased the 1st prize for this project by £200 to £460 - looking forward to seeing your app designs.
Just added football shirt icons, and the "GoalDash Arena" logo to assist with designs.
Project Deadline Extended
Reason: Extended to allow for revised submissions
Target Market(s)
Global Football Fans, low education level
Industry/Entity Type
It Company
Look and feel
Each slider illustrates characteristics of the customer's brand and the style your logo design should communicate.

```html
<!DOCTYPE html>
<html lang="en">
<head>
<meta charset="utf-8">
<title>GoalDash Arena – How it Works</title>
<link rel="stylesheet" href="https://fonts.googleapis.com/css2?family=Source+Sans+3:wght@400;600;700&display=swap">
<style>
  :root {
    --page: #0f1a0c;
    --photo-dark: #1c1e1c;
    --photo-mid: #4a4d4a;
    --photo-kit: #b9c93a;
    --panel: rgba(238, 238, 238, 0.9);
    --ink: #161616;
    --title-ink: #2d2d2d;
    --dash: #8a8a8a;
    --close-red: #d0140f;
    --nav-top: #66d94c;
    --nav-bottom: #2ba51b;
    --nav-divider: #1f7f14;
    --nav-text: #ffffff;
    --icon-ink: #153d10;
  }
  * { margin: 0; padding: 0; box-sizing: border-box; }
  html, body { width: 1200px; height: 2250px; overflow: hidden; background: var(--page); }
  body { font-family: "Source Sans 3", "Myriad Pro", sans-serif; }

  .app-screen { position: relative; width: 1200px; height: 2250px; overflow: hidden; }

  .hero-photo {
    position: absolute; inset: 0 0 182px 0;
    background:
      radial-gradient(ellipse 45% 35% at 85% 35%, var(--photo-kit) 0%, rgba(185,201,58,0.3) 45%, transparent 75%),
      radial-gradient(ellipse 70% 50% at 60% 40%, var(--photo-mid) 0%, transparent 70%),
      linear-gradient(180deg, #2a2c2a 0%, var(--photo-dark) 60%, #101110 100%);
  }

  .status-band { position: absolute; left: 0; top: 0; width: 1200px; height: 68px; background: rgba(120,124,120,0.55); }

  .info-sheet { position: absolute; left: 83px; top: 255px; width: 1033px; height: 1558px; }
  .info-sheet svg.sheet-shape { position: absolute; inset: 0; }

  .close-tab { position: absolute; left: 0; top: 121px; width: 112px; height: 112px; }
  .close-tab span {
    position: absolute; left: 26px; top: 10px;
    font-weight: 700; font-size: 40px; color: var(--ink);
  }

  .sheet-title {
    position: absolute; left: 0; right: 0; top: 160px;
    display: flex; justify-content: center; align-items: center; gap: 22px;
    color: var(--title-ink); font-weight: 600; font-size: 52px; letter-spacing: 0.5px;
  }
  .title-icon { width: 92px; height: 92px; }
  .title-rule { position: absolute; left: 20px; right: 20px; top: 252px; border-top: 4px dashed var(--dash); }

  .rules-list { position: absolute; left: 58px; right: 101px; top: 350px; list-style: none; }
  .rules-list li {
    position: relative; padding-left: 60px; margin-bottom: 52px;
    font-size: 39px; font-weight: 600; line-height: 48px; color: var(--ink);
    hyphens: manual;
  }
  .rules-list li svg { position: absolute; left: 0; top: 6px; width: 40px; height: 40px; }

  .tab-bar {
    position: absolute; left: 0; bottom: 0; width: 1200px; height: 182px;
    display: flex; background: linear-gradient(180deg, var(--nav-top), var(--nav-bottom));
  }
  .tab-item {
    display: flex; flex-direction: column; align-items: center; justify-content: center; gap: 8px;
    color: var(--nav-text); font-weight: 600; font-size: 43px; letter-spacing: 0.5px;
    border-right: 3px solid var(--nav-divider);
  }
  .tab-item:last-child { border-right: none; }
  .tab-item svg { width: 54px; height: 54px; }
  .tab-home { width: 260px; }
  .tab-leaderboards { width: 417px; }
  .tab-game { width: 245px; }
  .tab-social { width: 278px; }
</style>
</head>
<body>
<main class="app-screen">
  <div class="hero-photo" role="img" aria-label="Photo of a footballer in a yellow kit striking the ball on a dark pitch"></div>

  <div class="status-band"></div>

  <section class="info-sheet" aria-labelledby="sheet-heading">
    <svg class="sheet-shape" viewBox="0 0 1033 1558" aria-hidden="true">
      <path fill="var(--panel)" d="M20,121 H230 C270,121 270,70 300,40 C330,10 380,0 516,0 C652,0 703,10 733,40 C763,70 763,121 803,121 H1013 Q1033,121 1033,141 V1291 Q1033,1311 1013,1311 H803 C763,1311 770,1360 750,1420 C720,1520 650,1558 516,1558 C382,1558 312,1520 282,1420 C262,1360 270,1311 230,1311 H20 Q0,1311 0,1291 V141 Q0,121 20,121 Z"/>
    </svg>

    <div class="close-tab">
      <svg viewBox="0 0 112 112" width="112" height="112" aria-hidden="true">
        <path d="M20 0 H112 L0 112 V20 Q0 0 20 0 Z" fill="var(--close-red)"/>
      </svg>
      <span>x</span>
    </div>

    <h1 class="sheet-title" id="sheet-heading">
      <svg class="title-icon" viewBox="0 0 92 92" aria-hidden="true">
        <rect x="14" y="18" width="52" height="66" rx="8" fill="#3a3a3a" transform="rotate(-12 40 51)"/>
        <rect x="20" y="26" width="40" height="48" rx="3" fill="#4fbf3a" transform="rotate(-12 40 51)"/>
        <circle cx="64" cy="22" r="10" fill="#e2a04a"/>
      </svg>
      How it Works
    </h1>
    <div class="title-rule"></div>

    <ul class="rules-list">
      <li><svg viewBox="0 0 40 40" aria-hidden="true"><circle cx="20" cy="20" r="14" fill="var(--ink)"/><circle cx="20" cy="20" r="5" fill="#eee"/></svg>Select the match you want to make your pre&shy;diction on.</li>
      <li><svg viewBox="0 0 40 40" aria-hidden="true"><circle cx="20" cy="20" r="14" fill="var(--ink)"/><circle cx="20" cy="20" r="5" fill="#eee"/></svg>Give a thumbs-up to the outcome you predict will happen.</li>
      <li><svg viewBox="0 0 40 40" aria-hidden="true"><circle cx="20" cy="20" r="14" fill="var(--ink)"/><circle cx="20" cy="20" r="5" fill="#eee"/></svg>You will GAIN point if your predicted outcome becomes MORE LIKELY.</li>
      <li><svg viewBox="0 0 40 40" aria-hidden="true"><circle cx="20" cy="20" r="14" fill="var(--ink)"/><circle cx="20" cy="20" r="5" fill="#eee"/></svg>You will lose points if your predicted outcome becomes LESS LIKELY.</li>
      <li><svg viewBox="0 0 40 40" aria-hidden="true"><circle cx="20" cy="20" r="14" fill="var(--ink)"/><circle cx="20" cy="20" r="5" fill="#eee"/></svg>You can change your prediction at any time before or during the match.</li>
    </ul>
  </section>

  <nav class="tab-bar">
    <div class="tab-item tab-home">
      <svg viewBox="0 0 24 24" aria-hidden="true"><path d="M12 3 L2 12 H5 V21 H10 V15 H14 V21 H19 V12 H22 Z" fill="var(--icon-ink)"/></svg>
      HOME
    </div>
    <div class="tab-item tab-leaderboards">
      <svg viewBox="0 0 24 24" aria-hidden="true"><rect x="3" y="4" width="18" height="13" rx="1" fill="none" stroke="var(--icon-ink)" stroke-width="2"/><path d="M6 13 L10 9 L13 12 L18 7" fill="none" stroke="var(--icon-ink)" stroke-width="2"/><path d="M12 17 V21 M8 21 H16" stroke="var(--icon-ink)" stroke-width="2"/></svg>
      LEADERBOARDS
    </div>
    <div class="tab-item tab-game">
      <svg viewBox="0 0 24 24" aria-hidden="true"><path d="M6 3 H18 V9 A6 6 0 0 1 6 9 Z" fill="var(--icon-ink)"/><path d="M6 5 H2 V8 A4 4 0 0 0 6 11 M18 5 H22 V8 A4 4 0 0 1 18 11" fill="none" stroke="var(--icon-ink)" stroke-width="2"/><rect x="10.5" y="14" width="3" height="4" fill="var(--icon-ink)"/><rect x="7" y="18" width="10" height="3" fill="var(--icon-ink)"/></svg>
      GAME
    </div>
    <div class="tab-item tab-social">
      <svg viewBox="0 0 24 24" aria-hidden="true"><ellipse cx="10" cy="9" rx="8" ry="6" fill="var(--icon-ink)"/><path d="M5 13 L3 18 L9 14 Z" fill="var(--icon-ink)"/><ellipse cx="16" cy="15" rx="6" ry="4.5" fill="var(--icon-ink)"/><path d="M19 18 L21 22 L16 19 Z" fill="var(--icon-ink)"/></svg>
      SOCIAL
    </div>
  </nav>
</main>
</body>
</html>
```